Brightwire Hollow Business cards

one side I would like my logo (uploaded) and the other side I want my details. I'm an electrician in sydney. The logo side I'm happy with just a white background and our logo in the middle.

Details for other side
24/7 Sydney Electrician
Marcus Pell
0431 587 219
marcus@brightwirehollow.com.au
brightwirehollow.com.au
icons for facebook, instagram, linked in

Industry/Entity Type

electrician

Contact Information for Business Card

company info

```html
<!DOCTYPE html>
<html lang="en">
<head>
<meta charset="utf-8">
<title>Brightwire Hollow — Business Cards</title>
<link href="https://fonts.googleapis.com/css2?family=Open+Sans:ital,wght@0,400;0,600;0,700;1,700&display=swap" rel="stylesheet">
<style>
  :root {
    --backdrop: #808080;
    --card: #ffffff;
    --brand-red: #e8352a;
    --ink: #111111;
    --muted: #6b6b6b;
    --tag-grey: #7a7a7a;
  }
  * { margin: 0; padding: 0; box-sizing: border-box; }
  html, body { width: 1200px; height: 1000px; overflow: hidden; }
  body {
    background: var(--backdrop);
    font-family: "Open Sans", Arial, sans-serif;
    position: relative;
  }
  .card {
    position: absolute;
    width: 613px;
    height: 351px;
    background: var(--card);
    border-radius: 26px;
  }
  .card--front { left: 293px; top: 117px; }
  .card--back { left: 294px; top: 520px; }

  .wordmark {
    position: absolute;
    left: 0; right: 0;
    text-align: center;
    color: var(--brand-red);
    font-weight: 700;
    letter-spacing: 1px;
    white-space: nowrap;
  }
  .wordmark span { display: block; }
  .card--front .wordmark { top: 142px; font-size: 27px; line-height: 32px; }
  .card--back .wordmark { top: 44px; font-size: 21px; line-height: 26px; }

  .tagline {
    position: absolute;
    left: 0; right: 0;
    top: 258px;
    text-align: center;
    font-style: italic;
    font-weight: 700;
    font-size: 16px;
    color: var(--tag-grey);
    display: flex;
    justify-content: center;
    align-items: center;
    gap: 3px;
  }
  .tagline__hours { color: var(--brand-red); font-size: 18px; }
  .tagline__bolt { width: 9px; height: 18px; }

  .holder-name {
    position: absolute;
    right: 334px;
    top: 173px;
    font-size: 17px;
    font-weight: 600;
    letter-spacing: 2px;
    color: var(--ink);
    white-space: nowrap;
  }
  .divider {
    position: absolute;
    left: 300px;
    top: 162px;
    width: 2px;
    height: 52px;
    background: var(--brand-red);
  }
  .contact-list {
    position: absolute;
    left: 320px;
    top: 155px;
    list-style: none;
  }
  .contact-list li {
    display: flex;
    align-items: center;
    gap: 8px;
    height: 20px;
    font-size: 15px;
    color: var(--muted);
    white-space: nowrap;
  }
  .contact-list svg { width: 13px; height: 13px; fill: var(--brand-red); }

  .social-row {
    position: absolute;
    left: 0; right: 0;
    top: 303px;
    display: flex;
    justify-content: center;
    gap: 10px;
  }
  .social-dot {
    width: 20px; height: 20px;
    border-radius: 50%;
    background: var(--brand-red);
  }
</style>
</head>
<body>

<section class="card card--front" aria-label="Card front">
  <div class="wordmark"><span>BRIGHTWIRE</span><span>HOLLOW</span></div>
  <p class="tagline">
    <svg class="tagline__bolt" viewBox="0 0 9 18" aria-hidden="true"><path d="M6 0 L0 10 H4 L2 18 L9 7 H5 L7 0 Z" fill="var(--brand-red)"/></svg>
    <span class="tagline__hours">24/7</span>
    <span>SYDNEY ELECTRICIAN</span>
  </p>
</section>

<section class="card card--back" aria-label="Card back">
  <div class="wordmark"><span>BRIGHTWIRE</span><span>HOLLOW</span></div>

  <div class="holder-name">MARCUS PELL</div>
  <div class="divider"></div>
  <ul class="contact-list">
    <li>
      <svg viewBox="0 0 24 24" aria-hidden="true"><path d="M6.6 10.8a15.1 15.1 0 0 0 6.6 6.6l2.2-2.2a1 1 0 0 1 1-.25 11.4 11.4 0 0 0 3.6.57 1 1 0 0 1 1 1V20a1 1 0 0 1-1 1A17 17 0 0 1 3 4a1 1 0 0 1 1-1h3.5a1 1 0 0 1 1 1c0 1.25.2 2.45.57 3.57a1 1 0 0 1-.25 1z"/></svg>
      0431 587 219
    </li>
    <li>
      <svg viewBox="0 0 24 24" aria-hidden="true"><path d="M2 5h20v3l-10 6L2 8z"/><path d="M2 10l10 6 10-6v9H2z"/></svg>
      marcus@brightwirehollow.com.au
    </li>
    <li>
      <svg viewBox="0 0 24 24" aria-hidden="true"><path d="M12 2a10 10 0 1 0 0 20 10 10 0 0 0 0-20zm6.9 6h-2.9a15 15 0 0 0-1.4-3.6A8 8 0 0 1 18.9 8zM12 4c.8 1.2 1.5 2.5 1.9 4h-3.8c.4-1.5 1.1-2.8 1.9-4zM4.3 14a8 8 0 0 1 0-4h3.4a16 16 0 0 0 0 4zm.8 2h2.9c.3 1.3.8 2.5 1.4 3.6A8 8 0 0 1 5.1 16zM8 8H5.1a8 8 0 0 1 4.3-3.6C8.8 5.5 8.3 6.7 8 8zm4 12c-.8-1.2-1.5-2.5-1.9-4h3.8c-.4 1.5-1.1 2.8-1.9 4zm2.3-6H9.7a14 14 0 0 1 0-4h4.6a14 14 0 0 1 0 4zm.3 5.6c.6-1.1 1.1-2.3 1.4-3.6h2.9a8 8 0 0 1-4.3 3.6zm1.7-5.6a16 16 0 0 0 0-4h3.4a8 8 0 0 1 0 4z"/></svg>
      brightwirehollow.com.au
    </li>
  </ul>

  <div class="social-row" aria-label="Social profiles">
    <span class="social-dot" role="img" aria-label="Social profile one"></span>
    <span class="social-dot" role="img" aria-label="Social profile two"></span>
    <span class="social-dot" role="img" aria-label="Social profile three"></span>
  </div>
</section>

</body>
</html>
```